Ferris Contracting LLC Business Card Design

I am looking for a creative and unique business card design. We are a commercial construction general contractor. With the name "FERRIS" Contracting, I am hoping to see some neat designs that correlate with the name.

```html
<!DOCTYPE html>
<html lang="en">
<head>
<meta charset="utf-8">
<title>Ferris Contracting LLC – Business Card</title>
<link href="https://fonts.googleapis.com/css2?family=Montserrat:wght@500;800&family=Exo+2:wght@400&display=swap" rel="stylesheet">
<style>
  :root {
    --backdrop: #d4d5d7;
    --card-white: #ffffff;
    --card-black: #0e0f10;
    --brand-blue: #1f73c4;
    --text-light: #f2f2f2;
    --edge-blue: #1a6fd0;
  }
  * { margin: 0; padding: 0; box-sizing: border-box; }
  html, body { width: 1200px; height: 800px; overflow: hidden; }
  body { background: var(--backdrop); position: relative; font-family: "Exo 2", sans-serif; }

  .card {
    position: absolute;
    width: 540px;
    height: 309px;
    border-bottom: 2px solid var(--edge-blue);
    box-shadow: 0 10px 24px rgba(0,0,0,0.22);
  }
  .card-front { left: 40px; top: 140px; background: var(--card-white); }
  .card-back { left: 620px; top: 350px; background: var(--card-black); color: var(--text-light); }

  .wordmark {
    position: absolute;
    display: flex;
    align-items: center;
    gap: 14px;
    font-family: "Montserrat", sans-serif;
    font-weight: 800;
    color: var(--brand-blue);
    white-space: nowrap;
  }
  .wordmark-mark { border-radius: 50%; background: var(--brand-blue); flex: none; }
  .card-front .wordmark { left: 50%; top: 50%; transform: translate(-50%, -50%); font-size: 34px; letter-spacing: 1px; }
  .card-front .wordmark-mark { width: 30px; height: 30px; }
  .card-back .wordmark { left: 34px; top: 34px; font-size: 16px; gap: 8px; }
  .card-back .wordmark-mark { width: 14px; height: 14px; }

  .person { position: absolute; right: 40px; top: 40px; text-align: left; }
  .person-name { font-family: "Montserrat", sans-serif; font-weight: 800; font-size: 24px; color: var(--brand-blue); letter-spacing: 0.5px; }
  .person-title { font-family: "Montserrat", sans-serif; font-weight: 500; font-size: 11px; margin-top: 2px; }

  .contact-list { position: absolute; right: 30px; top: 160px; list-style: none; font-size: 12px; }
  .contact-list li { display: flex; align-items: center; gap: 8px; margin-bottom: 7px; }
  .contact-list .phone { font-size: 13px; letter-spacing: 3px; }
  .contact-list svg { width: 13px; height: 13px; fill: var(--brand-blue); flex: none; }

  .address { position: absolute; left: 34px; bottom: 36px; font-size: 13px; line-height: 1.8; letter-spacing: 0.5px; }
</style>
</head>
<body>
  <section class="card card-front">
    <div class="wordmark"><span class="wordmark-mark"></span>FERRIS CONTRACTING</div>
  </section>

  <section class="card card-back">
    <div class="wordmark"><span class="wordmark-mark"></span>FERRIS CONTRACTING</div>

    <div class="person">
      <div class="person-name">DAN KESSLER</div>
      <div class="person-title">Co-Founder &amp; President</div>
    </div>

    <ul class="contact-list">
      <li class="phone">
        <svg viewBox="0 0 24 24" aria-hidden="true"><path d="M6.6 10.8a15.1 15.1 0 0 0 6.6 6.6l2.2-2.2a1 1 0 0 1 1-.25 11.4 11.4 0 0 0 3.6.57 1 1 0 0 1 1 1V20a1 1 0 0 1-1 1A17 17 0 0 1 3 4a1 1 0 0 1 1-1h3.5a1 1 0 0 1 1 1c0 1.25.2 2.45.57 3.6a1 1 0 0 1-.25 1z"/></svg>
        555-014-2387
      </li>
      <li>
        <svg viewBox="0 0 24 24" aria-hidden="true"><path d="M2 5h20v14H2z M2 5l10 8 10-8" stroke="#0e0f10" stroke-width="1.5"/></svg>
        info@ferriscontractingusa.com
      </li>
      <li>
        <svg viewBox="0 0 24 24" aria-hidden="true"><circle cx="12" cy="12" r="10" fill="none" stroke="#1f73c4" stroke-width="2"/><path d="M2 12h20M12 2c3 3 3 17 0 20M12 2c-3 3-3 17 0 20" fill="none" stroke="#1f73c4" stroke-width="1.5"/></svg>
        www.ferriscontractingusa.com
      </li>
    </ul>

    <address class="address" style="font-style:normal">
      1420 North Alder Rd<br>
      Springdale, MO 64000
    </address>
  </section>
</body>
</html>
```